Website front end design for an education nonprofit

This project involves design and development of the website front end (i.e., Web user interface and user experience design) for PAVO Tides, a nonprofit initiative for developing an online platform for basic English language instruction, especially targeted toward underprivileged, non-native English speaking populations.

More about us: We are a team of educators, researchers and engineers passionate about this cause and would like to invite talented, creative web developers to join us in this effort to create positive social impact! Please send a personal message to the project owner for the executive summary to get more information about our initiative, big picture vision and the team.

PAVO Tides website front end (UI/UX) design
Our key goals for this project are to develop an impressive Drupal-based front end for our website as well as to find really talented and creative web/UI/UX designers-cum-developers who are experts in the state-of-the-art web technologies, and are passionate about the cause of global online basic education. At the end of this project, we hope to have long term engagement with the selected developer(s) for our future website design and development needs.

Here are some preliminary guidelines on the PAVO Tides website front end framework as envisioned by us so far. Please note that we would very much encourage creative ideas and mock-ups from the developers.

1. Current platform: Our website prototype back-end uses Drupal CMS (we plan to continue using Drupal CMS) and at the moment, a toy front-end is based on the Drupal Skeleton platform for its simplicity, clean UI and mobile device friendliness. The web developer / designer can choose any Drupal front end as a starting point or come up with a new Drupal template that meets our requirements below. Prior experience and expertise on Drupal would be great.

2. Audience profile: While the primary audience for the website is expected to be young kids (6-10 years) not very familiar with English, the secondary audience also includes adults interested in basic English language skills. So the overall goal is to have simple, uncluttered / clean, elegant and lightweight (think loading time as well as mobile device friendliness) interface that is extremely intuitive and easy to navigate, is artistic and aesthetically appealing to a wide audience (especially the non-native English speaking populations). The most important point is that our target audience should feel welcome with the clean, crisp look and easy, user-centric navigation, and should in no case feel overwhelmed (say with too much text or clutter on the front page).

3. Front page: Here is a currently envisioned preliminary sketch of the website front page (very much open for refinement and improvements)
a. The top “menu bar” part of the landing page will have our organization name and logo along with (or above) the top menu bar with the following links and sub-links
i. “Learn” link with sub-menu of all our content sections (World learning, Basic sentence learning, Classic short stories, Picture Dictionary)
ii. “About” links with information about us (sub-menu entries: About PAVO Tides, Team, Supporters, Contributors)
iii. “Contribute” link with sub-menu entries Donate, Volunteer
iv. Menu entries towards the right side: “Login / sign up” followed by
v. “Search” with space to enter the search phrase
b. The middle “main page content” part of the page is where we would have entry points to our main content categories. The portion is envisioned to be graphical, with big blocks (images) as links to our content categories. The current categories (to start with) include 1. Word learning, 2. Basic sentence learning, and 3. Classic stories. We welcome creative ideas to represent these content categories in an appealing and elegant way (for example, these content categories could be portrayed as closed double doors that lead to the pages with the content. We would like to have placeholders for appropriate image links to different content categories – we should be able to put appropriate images or change them as we come up with new ideas that would work best with our target audience). The categories would change and grow as our content evolves, hence the core idea is to build a flexible framework that readily allows for expansion as well as customization.
c. The bottom menu / links bar portion of the landing page will have a list of links that are not included at the top. Examples include (with flexibility needed to add more when needed)
i. “Help”: this leads to a new page with FAQ, How to use
ii. “Contact us” link to a web contact form page
iii. “For Teachers” link to a page with information such as how to use, tips, pilot programs,
iv. “Volunteer” link to page with links such as Donate, Volunteer
v. “Contributors” that would link to a page with information about our Artists, Teachers, Writers, Developers etc.
vi. “Jobs” would link to a jobs page
vii. “Blog” would lead to our blog page
viii. “User stories” link to pages with feedback that we obtain from the users about how the content has helped them,
ix. Web 2.0 placeholders for social media (to be added later)

d. The footer of the website should include text “2013 PAVO Tides, All rights reserved.”

4. The middle block of the front page is the largest in screen real estate and perhaps the most challenging part that requires much creativity and thought on the UI/UX design aspect – the content pages pointed to by the section links on the middle portion of the front page are also being designed.

5. Color preference is towards soft, elegant (think grays, whites, light blues, other light colors) web safe colors. No harsh (too bright, garish) colors.

6. Fonts preference Nice, clean looking fonts (Arial alright) compatible across browsers.

7. Portability and robustness of the front page layout for different platforms should be carefully considered. Although our first launch target platform is PC (where cross browser compatibility is important), this would very soon be followed by mobile devices such as tablets and smartphones given their prevalence across the globe. This mobile friendly design or easy portability to mobile platforms with little work requirement should be considered as a design requirement.

8. Front page as a framework for the complete website: Note that the top and the bottom portions of the front page are envisioned be used as a common template / frame across all the pages of our website – the middle portion would be used to show our content on the other pages of our website.

9. UX: For the UI/UX design, it is critical to keep in mind key qualities such as ease of use, simplicity, elegance and artistic appeal. Some specific points to keep in mind: (1) the major portion of the target audience would be new to English and (2) young children are expected to be the primary audience but we want the website to appeal to adults interested in learning as well, and (3) we need the website to work even with relatively slow Internet speeds (for underdeveloped / developing regions especially), should always be kept in mind. HTML5 compliance ideas are encouraged.

10. Strictly not desired: Typical corporate feel seen in many webpages, blocky graphics, dull and uninviting overall look with no personality, Flash type effects, harsh colors.

11. Creativity and imagination necessary: We would like to reiterate that the designer/developer has complete freedom to re-imagine the front page considering the above requirements and get back with ideas for an inspiring layout that presents the content outlined above in an intuitive format, carefully considering our target audience.

A note: As a rule, we will always make sure that our developers and artists get proper credit for their work and are recognized and acknowledged by everyone visiting our website.

Expected deliverables:
Website design psd files AND coded webpage / Drupal template: the corresponding source code and all the required libraries, images etc would be required with minimal documentation / pointers on how to make changes and customizations.

Interested developers are encouraged to first send us preliminary prototype Design for the front page to get feedback on whether their approach and style is in line with our needs and preferences. We will suggest the developers to proceed further if the team thinks there is some potential for a match (of course, the final determination would be from the pool of shortlisted submissions) – otherwise, in case the team does not see potential for a match with our needs or if we have already received multiple submissions that are comparatively more closely aligned with our vision for the website, we'd prefer to be respectful of the developers’ time and effort by requesting them not to proceed further.

Please consider this effort as your contribution to an important social cause of global and accessible online education and not a commercial enterprise (our passion for making a positive impact is what is driving the PAVO Tides nonprofit team to undertake this initiative!). We would like to invite you to join us in this effort!

Reason: Due to requests from interested designers, we are extending the deadline. Looking forward to receiving many other creative designs!

Please see the project brief.

• Please see the project brief.

```html
<!DOCTYPE html>
<html lang="en">
<head>
<meta charset="utf-8">
<title>PAVO Tides</title>
<link href="https://fonts.googleapis.com/css2?family=PT+Sans+Narrow:wght@400;700&family=PT+Sans:wght@400;700&family=Montserrat:wght@400&display=swap" rel="stylesheet">
<style>
:root{
  --brand:#1f86c4;
  --heading:#17608f;
  --nav:#4a4a4a;
  --text:#333;
  --muted:#555;
  --btn-top:#2f96d6;
  --btn-bot:#0d5a93;
  --bar-top:#8a8a8a;
  --bar-bot:#3b3b3b;
  --foot-top:#8b8485;
  --foot-bot:#4d4646;
  --white:#fff;
}
*{box-sizing:border-box;margin:0;padding:0}
html,body{width:1088px;height:1200px;overflow:hidden;background:var(--white)}
body{position:relative;font-family:Arial,Helvetica,sans-serif;color:var(--text)}
.abs{position:absolute}
.logo{left:142px;top:46px;font-family:"PT Sans Narrow",sans-serif;font-weight:700;font-size:36px;color:var(--brand);letter-spacing:.5px;white-space:nowrap}
.nav a{position:absolute;top:65px;font-family:"PT Sans",sans-serif;font-size:12px;color:var(--nav);text-decoration:none;letter-spacing:.2px}
.btn{display:flex;align-items:center;justify-content:center;color:var(--white);background:linear-gradient(var(--btn-top),var(--btn-bot));border-radius:3px;font-family:"PT Sans",sans-serif;text-decoration:none}
.btn-top{top:58px;width:84px;height:25px;font-size:12px;letter-spacing:.3px}
.search{left:775px;top:52px;width:184px;height:33px;border:1px solid #cfcfcf;border-radius:4px;background:linear-gradient(#fafafa,#ececec);font-size:10px;color:#3d5a1f;padding:10px 0 0 7px}
.search svg{position:absolute;right:12px;top:10px}
.hero{left:126px;top:109px;width:835px;height:325px;border:1px solid #d8d8d8;background:linear-gradient(100deg,#e9e6e2 0%,#d8cdc2 45%,#b9a6a0 70%,#8f90cf 85%,#d2c6bc 100%)}
.hero-caption{left:175px;top:255px;width:540px;font-family:"PT Sans Narrow",sans-serif;font-size:13.5px;line-height:22px;color:#111}
.arrow{top:162px;width:35px;height:35px;border-radius:5px;background:#1e1e1e;color:#ddd;display:flex;align-items:center;justify-content:center;font-size:18px}
.cats{left:126px;top:445px;width:835px;height:68px;background:linear-gradient(var(--bar-top) 0%,#6a6a6a 50%,var(--bar-bot) 100%)}
.cats .div{position:absolute;top:0;width:2px;height:68px;background:linear-gradient(#9a9a9a,#2c2c2c)}
.cat{position:absolute;top:0;height:68px;display:flex;align-items:center;gap:14px;color:var(--white);font-weight:700;font-size:14.5px;letter-spacing:.2px}
.welcome h1{position:absolute;left:127px;top:540px;font-family:"PT Sans Narrow",sans-serif;font-size:19.5px;color:var(--heading);font-weight:700;letter-spacing:.2px}
.welcome p{position:absolute;left:127px;top:583px;width:820px;font-family:Montserrat,sans-serif;font-size:11.8px;line-height:22px;color:var(--text)}
.card{position:absolute;top:703px;width:274px}
.card .pic{width:274px;height:141px;border:2px solid #c8c8c8}
.card h2{margin-top:14px;font-family:"PT Sans Narrow",sans-serif;font-size:14px;color:var(--heading);font-weight:700;letter-spacing:.1px}
.card p{margin-top:9px;font-size:11px;line-height:17px;color:var(--muted)}
.card .btn{margin-top:11px;width:75px;height:26px;font-family:Arial,sans-serif;font-size:10.5px;border-radius:2px}
footer{position:absolute;left:0;top:1003px;width:1088px;height:197px;background:linear-gradient(var(--foot-top),var(--foot-bot));color:var(--white)}
footer h3{position:absolute;font-family:"PT Sans",sans-serif;font-weight:400;font-size:17px;letter-spacing:.2px}
footer .link{position:absolute;font-family:"PT Sans",sans-serif;font-size:12.8px;color:var(--white)}
.news-sub{left:497px;top:42px;font-size:11px}
.news-input{left:495px;top:65px;width:181px;height:27px;background:var(--white);border:1px solid #bbb;color:#222;font-size:9.5px;padding:7px 0 0 6px}
.news-submit{left:498px;top:111px;width:68px;height:28px;background:linear-gradient(#9c9c9c,#3a3a3a);font-family:"PT Sans",sans-serif;font-weight:700;font-size:13px;display:flex;align-items:center;justify-content:center}
.copy{left:434px;top:163px;font-size:11px}
.social{position:absolute;left:777px;display:flex;align-items:center;gap:11px;font-family:"PT Sans",sans-serif;font-size:12.8px}
.social i{width:23px;height:23px;border-radius:50%;background:linear-gradient(#f4f4f4,#bdbdbd);display:block}
</style>
</head>
<body>
<header>
  <div class="abs logo">PAVO Tides</div>
  <nav class="nav">
    <a style="left:341px">LEARN</a>
    <a style="left:410px">ABOUT</a>
    <a style="left:489px">CONTRIBUTE</a>
  </nav>
  <a class="abs btn btn-top" style="left:585px">SIGN UP</a>
  <a class="abs btn btn-top" style="left:683px">LOGIN</a>
  <div class="abs search">Search
    <svg width="13" height="13" viewBox="0 0 13 13"><circle cx="5" cy="5" r="3.6" fill="none" stroke="#222" stroke-width="2"/><line x1="7.6" y1="7.6" x2="12" y2="12" stroke="#222" stroke-width="2.4" stroke-linecap="round"/></svg>
  </div>
</header>

<section class="abs hero" role="img" aria-label="Photo of a smiling student learning on a laptop">
  <div class="abs arrow" style="left:4px">&#8249;</div>
  <div class="abs arrow" style="left:794px">&#8250;</div>
  <p class="abs hero-caption">Lorem ipsum dolor sit amet, consectetur adipisicing elit, sed do eiusmod tempor incidt. Duis aute , sed do eiusmod tempor incidt. Duis aute irure dolor in reprehenderit in voluptate velit esse cillum</p>
</section>

<section class="abs cats">
  <div class="div" style="left:271px"></div>
  <div class="div" style="left:574px"></div>
  <a class="cat" style="left:71px">
    <svg width="27" height="34" viewBox="0 0 27 34"><path d="M2 1h17l6 6v26H2z" fill="#f2f2f2"/><path d="M19 1v6h6" fill="#ccc"/><rect x="0" y="4" width="13" height="6" fill="#555"/><g stroke="#777" stroke-width="1"><line x1="6" y1="15" x2="20" y2="15"/><line x1="6" y1="19" x2="20" y2="19"/><line x1="6" y1="23" x2="17" y2="23"/><line x1="6" y1="27" x2="19" y2="27"/></g></svg>
    WORD LEARNING</a>
  <a class="cat" style="left:303px">
    <svg width="44" height="36" viewBox="0 0 44 36"><path d="M2 22 22 12l20 10-20 11z" fill="#e6e6e6"/><path d="M2 22v4l20 10 20-10v-4L22 33z" fill="#9a9a9a"/><path d="M10 18 28 6l4 4-16 12z" fill="#f5f5f5"/><line x1="30" y1="2" x2="22" y2="20" stroke="#fff" stroke-width="2.5"/></svg>
    BASIC SENTENCE LEARNING</a>
  <a class="cat" style="left:596px">
    <svg width="28" height="38" viewBox="0 0 28 38"><rect x="3" y="12" width="22" height="24" fill="#cfcfcf"/><rect x="7" y="16" width="14" height="16" fill="#777"/><rect x="11" y="2" width="6" height="10" fill="#eee"/></svg>
    CLASSIC SHORT STORIES</a>
</section>

<main class="welcome">
  <h1>WELCOME TO OUR COMPANY</h1>
  <p>Lorem ipsum dolor sit amet, consectetur adipisicing elit, sed do eiusmod tempor incidt. Duis aute irure dolor in reprehenderit in voluptate velit esse cillum Lorem ipsum dolor sit amet, consectetur adipisicing elit, sed do eiusmod tempor incidt. Duis aute irure dolor in reprehenderit in voluptate velit esse cillumLorem ipsum dolor sit amet, consectetur adipisicing elit, sed do eiusmod tempor incidt. Duis aute irure dolor in reprehenderit in voluptate velit esse cillum</p>

  <article class="card" style="left:126px">
    <div class="pic" role="img" aria-label="Photo of two students studying together" style="background:linear-gradient(90deg,#d9d2cb,#c7a99a 45%,#b27bb0 75%,#e8e2dc)"></div>
    <h2>DUIS AUTE IRURE DOLOR IN REPREHENDERIT</h2>
    <p>Lorem ipsum dolor sit amet, consectetuer adipiscing elit. Nndimentum at, laoreet mattis, massa.</p>
    <a class="btn">READ MORE</a>
  </article>
  <article class="card" style="left:407px">
    <div class="pic" role="img" aria-label="Photo of a young student reading in a classroom" style="background:linear-gradient(90deg,#b2542e,#8a6a5c 40%,#a9a6b4 60%,#c98a4c)"></div>
    <h2>DUIS AUTE IRURE DOLOR IN REPREHENDERIT</h2>
    <p>Lorem ipsum dolor sit amet, consectetuer adipiscing elit. Nndimentum at, laoreet mattis, massa.</p>
    <a class="btn">READ MORE</a>
  </article>
  <article class="card" style="left:687px">
    <div class="pic" role="img" aria-label="Photo of a student writing in a notebook" style="background:linear-gradient(90deg,#7a6a5c,#d9b93a 40%,#e3c84a 60%,#ece8e2)"></div>
    <h2>DUIS AUTE IRURE DOLOR IN REPREHENDERIT</h2>
    <p>Lorem ipsum dolor sit amet, consectetuer adipiscing elit. Nndimentum at, laoreet mattis, massa.</p>
    <a class="btn">READ MORE</a>
  </article>
</main>

<footer>
  <h3 style="left:129px;top:22px">ABOUT</h3>
  <a class="link" style="left:132px;top:59px">About PAVO Tides</a>
  <a class="link" style="left:132px;top:91px">Team</a>
  <a class="link" style="left:132px;top:122px">Supporters</a>
  <a class="link" style="left:132px;top:154px">Contributors</a>
  <a class="link" style="left:329px;top:58px">Leaen</a>
  <a class="link" style="left:329px;top:90px">Team</a>
  <a class="link" style="left:329px;top:121px">About</a>
  <a class="link" style="left:329px;top:153px">Contribute</a>

  <h3 style="left:496px;top:23px">NEWSLETTER</h3>
  <div class="abs news-sub">Sing up for sneak peak updates !</div>
  <div class="abs news-input">Enter your email address</div>
  <div class="abs news-submit">SUBMIT</div>
  <div class="abs copy">Copyrights @ 2013 All Rights Reserved</div>

  <h3 style="left:774px;top:22px">GET CONNECTED</h3>
  <a class="social" style="top:47px"><i></i>Friendfold</a>
  <a class="social" style="top:75px"><i></i>Chirpline</a>
  <a class="social" style="top:103px"><i></i>Linkwork</a>
  <a class="social" style="top:131px"><i></i>RSS</a>
</footer>
</body>
</html>
```